BrightKeel Business Card Contest

We are looking for a modern business card that catches attention and is unique. Attached is the brand guide and logo files. Please note that the back side (not the side with our name and info) with be UV raise printed, so have fun with the design there. We want to include Name, Title, Phone number, email, website.

Contact Information for Business Card

Please see project description

```html
<!DOCTYPE html>
<html lang="en">
<head>
<meta charset="utf-8">
<title>BrightKeel Business Card</title>
<link href="https://fonts.googleapis.com/css2?family=Outfit:wght@400;500;600&display=swap" rel="stylesheet">
<style>
  :root {
    --bg: #d5d6d8;
    --white: #ffffff;
    --ink: #363944;
    --navy: #243a86;
    --royal: #2b5cb8;
    --sky: #3a8fe0;
    --cyan: #31d9ef;
    --ice: #c9dbe6;
    --orange: #f5a23a;
    --red: #e6432e;
  }
  html, body {
    margin: 0;
    width: 1200px;
    height: 952px;
    overflow: hidden;
    background: var(--bg);
    font-family: "Outfit", sans-serif;
  }
  .card {
    position: absolute;
    left: 320px;
    width: 560px;
    height: 320px;
    overflow: hidden;
    box-shadow: 0 18px 40px rgba(0,0,0,.18);
  }
  .card--front { top: 120px; background: var(--white); }
  .card--back { top: 512px; background: var(--navy); }

  .brand {
    position: absolute;
    display: flex;
    align-items: center;
    gap: 10px;
    font-weight: 500;
    letter-spacing: -0.5px;
  }
  .brand__square { width: 18px; height: 18px; background: currentColor; }
  .card--front .brand { left: 40px; top: 34px; font-size: 32px; color: var(--ink); }
  .card--back .brand { right: 44px; top: 60px; font-size: 46px; color: var(--white); }
  .card--back .brand__square { width: 26px; height: 26px; }

  .person { position: absolute; left: 40px; top: 98px; }
  .person__name { margin: 0; font-size: 24px; font-weight: 500; color: var(--royal); letter-spacing: 1px; }
  .person__title { margin: 2px 0 0; font-size: 14px; color: var(--sky); letter-spacing: 1.5px; }
  .divider {
    position: absolute; left: 0; top: 160px; width: 280px; height: 2px;
    background: linear-gradient(90deg, var(--royal), var(--sky) 40%, var(--orange) 75%, var(--red));
  }
  .contacts { position: absolute; left: 40px; top: 178px; margin: 0; padding: 0; list-style: none; }
  .contacts li { display: flex; align-items: center; gap: 10px; font-size: 12.5px; color: var(--royal); height: 24px; }
  .contacts svg { width: 13px; height: 13px; flex: none; }

  .facet-art { position: absolute; }
  .card--front .facet-art {
    left: 300px; top: 0; width: 260px; height: 320px;
    background: linear-gradient(100deg, var(--royal), var(--sky) 25%, var(--cyan) 45%, var(--ice) 65%, var(--orange) 85%, var(--red));
  }
  .card--back .facet-art {
    left: 0; top: 120px; width: 340px; height: 200px;
    background: linear-gradient(170deg, var(--red), var(--orange) 25%, var(--ice) 45%, var(--cyan) 68%, var(--sky) 85%, var(--royal));
  }
</style>
</head>
<body>
  <section class="card card--front">
    <div class="brand"><span class="brand__square"></span>BrightKeel</div>
    <div class="person">
      <p class="person__name">JOHN DOE</p>
      <p class="person__title">DIRECTOR</p>
    </div>
    <div class="divider"></div>
    <ul class="contacts">
      <li><svg viewBox="0 0 12 12"><path d="M6 1a3.5 3.5 0 0 0-3.5 3.5C2.5 7.5 6 11 6 11s3.5-3.5 3.5-6.5A3.5 3.5 0 0 0 6 1z" fill="var(--royal)"/><circle cx="6" cy="4.5" r="1.3" fill="#fff"/></svg>1234 Road Blvd, City, AA 7899</li>
      <li><svg viewBox="0 0 12 12"><path d="M3 1.5l2 2.2-1 1.3a6 6 0 0 0 3 3l1.3-1 2.2 2-1.2 1.5C5.5 10.5 1.5 6.5 1.5 2.7z" fill="var(--sky)"/></svg>123.456.789</li>
      <li><svg viewBox="0 0 12 12"><rect x="1" y="2.5" width="10" height="7" fill="var(--orange)"/><path d="M1 2.5l5 4 5-4" stroke="#fff" fill="none"/></svg>john@brightkeel.com</li>
      <li><svg viewBox="0 0 12 12"><path d="M6 1l4 5H7.5v5h-3V6H2z" fill="var(--red)"/></svg>www.brightkeel.com</li>
    </ul>
    <div class="facet-art" role="img" aria-label="Faceted geometric artwork in blue, cyan, pale blue, orange and red"></div>
  </section>

  <section class="card card--back">
    <div class="facet-art" role="img" aria-label="Faceted geometric artwork in red, orange, pale blue, cyan and blue"></div>
    <div class="brand"><span class="brand__square"></span>BrightKeel</div>
  </section>
</body>
</html>
```